One Page Magazine Ad for New Apartment in Calgary, AB Canada

We need a one page magazine ad for a new apartment community in Calgary, Alberta.

We pride ourselves in providing the highest level of customer service and the best amenities for our community.

COMMUNITY HIGHLIGHTS

- Brand new luxury apartment rental community in the exciting Calgary Beltline neighborhood
- 13 unique spacious floor plans fit for every lifestyle (1BR-1BATH, 2BR-1BATH & 2BR-2BATH)
- Professionally managed
- On-site staff during business hours to help you with any of your needs
- Pet-friendly community
- State of the art Fitness Facility
- 2 rooftop terraces outfitted with 8 Community Brixford BBQs
- Great area for entertaining guests and a safe spot to take your dog out for some fresh air without leaving the building
- 2 resident lounges with multimedia suite, 60-inch TVs, Zentra Duo, Silver Pin Arcade system, Poker table
- Great venues to host your next party, open 24/7 free to use and bookable by residents for free!
- Monthly resident events and parties hosted by the on-site staff
- Underground secured guest and resident parking available
- Electric Car Charging Stations
- Garbage & Recycling chutes on every floor
- Controlled Access/Building
- Gated Underground Parking Garage
- Adjacent to the Beltline neighborhood bike lane on 12th Avenue SW
- Elevators - Underground Secured Bike Storage and bike repair workstation
- On-site Maintenance
- Box Waiting Package Management System
- Additional Storage Available
- Footsteps away from the local Valemart Grocery and Valemart Wine Store
- Minutes away from the new free leash dog park Ridgewell Park

APARTMENT AMENITIES

- Gourmet Kitchen with 4 piece Stainless Steel Appliances (Stove, Fridge, Microwave and Dishwasher)
- In suite dryer and washer
- Large Closets
- Patio/Balcony
- City and mountain views
- Ceramic Tile and Laminate Hardwood Flooring
- Quartz Counter-tops
- Roller Blinds for all Windows
- Walk-in Closets

For branding style, floor plans, amenities and photos please visit our website www.stayatthefenwick.example

Target Market(s)

Young Adults and Recently Single Market

Industry/Entity Type

Real Estate

Font styles to use
Sans Serif

Colors
f37122

Requirements
Must have
• - Pictures of the community
• - Possibly use of a stock photo

```html
<!DOCTYPE html>
<html lang="en">
<head>
<meta charset="utf-8">
<title>The Fenwick – New Apartment Community in Calgary</title>
<link href="https://fonts.googleapis.com/css2?family=Open+Sans:wght@300;400;600;700&display=swap" rel="stylesheet">
<style>
  :root {
    --orange: #f37122;
    --orange-deep: #f4560c;
    --ink: #3a3a3a;
    --paper: #fdfcfb;
    --white: #ffffff;
    --frame: #111111;
  }
  * { margin: 0; padding: 0; box-sizing: border-box; }
  html, body { width: 923px; height: 1200px; overflow: hidden; background: var(--white); }
  body { font-family: "Open Sans", Arial, sans-serif; color: var(--ink); }
  .ad { position: relative; width: 923px; height: 1200px; background: var(--white); overflow: hidden; }
  .ad__frame { position: absolute; left: 59px; top: 38px; width: 803px; height: 1133px; border: 1.5px solid var(--frame); background: var(--paper); }
  .ad__art { position: absolute; inset: 0; width: 923px; height: 1200px; }

  .brand { position: absolute; left: 640px; top: 120px; display: flex; align-items: center; gap: 8px;
    font-weight: 400; font-size: 21px; letter-spacing: 3px; color: var(--ink); text-transform: uppercase; }
  .brand__mark { width: 14px; height: 14px; background: var(--orange); }

  .headline { position: absolute; left: 189px; top: 350px; color: var(--white); line-height: 1.1;
    text-shadow: 0 1px 3px rgba(90, 30, 5, 0.45); }
  .headline__strong { display: block; font-weight: 700; font-size: 32px; }
  .headline__place { display: block; font-weight: 300; font-size: 25px; margin-top: 4px; }

  .tagline { position: absolute; left: 0; width: 923px; top: 490px; text-align: center;
    font-weight: 300; font-size: 20.5px; line-height: 24px; color: var(--ink); text-transform: uppercase; }

  .gallery { position: absolute; top: 562px; left: 126px; display: flex; gap: 11px; }
  .gallery__photo { width: 157px; height: 157px; border-radius: 15px; }
  .gallery__photo--lounge { background: linear-gradient(180deg, #d8cfcb 0%, #a7433b 30%, #27406f 55%, #1f3158 85%, #2a2320 100%); }
  .gallery__photo--bedroom { background: linear-gradient(180deg, #e2e2de 0%, #c7c3bb 40%, #8d8176 70%, #5a4e45 100%); }
  .gallery__photo--terrace { background: linear-gradient(180deg, #d9b2a3 0%, #c4bab3 30%, #9b9894 55%, #3a3836 80%, #7d7a77 100%); }
  .gallery__photo--building { background: linear-gradient(180deg, #9fb6cb 0%, #a98468 30%, #b45a3f 60%, #7e4236 85%, #5b4f48 100%); }

  .section-title { position: absolute; font-weight: 400; font-size: 11.5px; line-height: 14px; color: var(--ink); text-transform: uppercase; }
  .section-title em { font-style: normal; color: var(--orange); }
  .section-title--highlights { left: 146px; top: 749px; }
  .section-title--amenities { left: 668px; top: 749px; }

  .rule { position: absolute; width: 2px; background: var(--orange); }
  .rule--highlights { left: 132px; top: 780px; height: 241px; }
  .rule--amenities { left: 629px; top: 780px; height: 237px; }

  .list { position: absolute; list-style: none; font-weight: 300; font-size: 12.2px; line-height: 14.5px; color: var(--ink); }
  .list li { position: relative; padding-left: 8px; }
  .list li::before { content: "·"; position: absolute; left: 0; font-weight: 700; }
  .list--highlights { left: 146px; top: 777px; width: 450px; }
  .list--amenities { left: 668px; top: 792px; width: 134px; hyphens: manual; }

  .contact { position: absolute; display: flex; align-items: center; gap: 11px; font-weight: 600; font-size: 13px; color: var(--ink); }
  .contact svg { flex: none; }
  .contact--phone { left: 124px; top: 1056px; }
  .contact--web { left: 124px; top: 1088px; }
  .contact--address, .contact--social { font-weight: 400; font-size: 10.5px; line-height: 13px; gap: 9px; }
  .contact--address { left: 414px; top: 1054px; }
  .contact--social { left: 414px; top: 1082px; }
</style>
</head>
<body>
<main class="ad">
  <div class="ad__frame"></div>
  <svg class="ad__art" viewBox="0 0 1152 1500">
    <defs>
      <linearGradient id="interiorTone" x1="0" y1="0" x2="1" y2="1">
        <stop offset="0" stop-color="#d8d8d8"/>
        <stop offset="0.5" stop-color="#9a9a9a"/>
        <stop offset="1" stop-color="#5e5e5e"/>
      </linearGradient>
      <linearGradient id="residentsTone" x1="0" y1="0" x2="1" y2="0">
        <stop offset="0" stop-color="#6f8f8a"/>
        <stop offset="0.35" stop-color="#e0a783"/>
        <stop offset="0.65" stop-color="#efcdb9"/>
        <stop offset="1" stop-color="#c8d8c8"/>
      </linearGradient>
      <linearGradient id="residentsShade" x1="0" y1="0" x2="0" y2="1">
        <stop offset="0.45" stop-color="#d9581a" stop-opacity="0"/>
        <stop offset="0.68" stop-color="#d9581a" stop-opacity="0.8"/>
        <stop offset="1" stop-color="#c24512" stop-opacity="1"/>
      </linearGradient>
      <linearGradient id="bandTone" x1="0" y1="0" x2="1" y2="0">
        <stop offset="0" stop-color="#c0440f"/>
        <stop offset="0.7" stop-color="#dd6428"/>
        <stop offset="1" stop-color="#ec8248" stop-opacity="0.8"/>
      </linearGradient>
    </defs>
    <path role="img" aria-label="Photo of a bright modern apartment living room"
      d="M74 140 C200 95 480 70 665 205 C560 215 470 260 400 300 C280 365 170 420 74 445 Z"
      fill="url(#interiorTone)"/>
    <path role="img" aria-label="Photo of two smiling young residents in a sunny apartment"
      d="M74 445 C170 420 280 365 400 300 C520 230 640 205 760 215 C900 225 1010 270 1075 320 L1075 505 C980 520 860 500 760 485 C700 540 560 600 400 590 C260 585 150 520 80 470 Z"
      fill="url(#residentsTone)"/>
    <path d="M74 445 C170 420 280 365 400 300 C520 230 640 205 760 215 C900 225 1010 270 1075 320 L1075 505 C980 520 860 500 760 485 C700 540 560 600 400 590 C260 585 150 520 80 470 Z"
      fill="url(#residentsShade)"/>
    <path d="M80 470 C150 520 260 585 400 590 C560 600 690 540 760 485 C600 520 420 470 200 460 C150 458 110 462 80 470 Z"
      fill="url(#bandTone)"/>
    <path d="M760 485 C880 430 980 360 1075 340 L1075 505 C980 515 860 505 760 485 Z" fill="var(--orange-deep)"/>
    <path d="M820 1355 C930 1345 1020 1310 1075 1270 L1075 1460 C990 1440 890 1400 820 1355 Z" fill="var(--orange-deep)"/>
  </svg>

  <div class="brand"><span class="brand__mark"></span>The Fenwick</div>

  <h1 class="headline">
    <span class="headline__strong">NEW</span>
    <span class="headline__strong">APPARTMENT COMMUNITY</span>
    <span class="headline__place">IN CALGARY, ALBERTA</span>
  </h1>

  <p class="tagline">We pride ourselves in providing the highest level of customer<br>service and the best amenities for our community</p>

  <div class="gallery">
    <div class="gallery__photo gallery__photo--lounge" role="img" aria-label="Photo of the resident lounge poker table"></div>
    <div class="gallery__photo gallery__photo--bedroom" role="img" aria-label="Photo of a furnished suite bedroom"></div>
    <div class="gallery__photo gallery__photo--terrace" role="img" aria-label="Photo of the rooftop terrace with giant chess set"></div>
    <div class="gallery__photo gallery__photo--building" role="img" aria-label="Photo of the apartment building exterior at sunset"></div>
  </div>

  <h2 class="section-title section-title--highlights">Community <em>Highlights</em></h2>
  <span class="rule rule--highlights"></span>
  <ul class="list list--highlights">
    <li>Brand new luxury apartment rental community in the exciting Calgary Beltline neighborhood</li>
    <li>13 unique spacious floor plans fit for every lifestyle (1BR-1BATH, 2BR-1BATH &amp; 2BR-2BATH)</li>
    <li>Professionally managed</li>
    <li>On-site staff during business hours to help you with any of your needs</li>
    <li>Pet-friendly community</li>
    <li>State of the art Fitness Facility</li>
    <li>2 rooftop terraces outfitted with 8 Community Brixford BBQs</li>
    <li>Great area for entertaining guests and a safe spot to take your dog out for some fresh air without leaving the building</li>
    <li>2 resident lounges with multimedia suite, 60-inch TVs, Zentra Duo, Silver Pin Arcade system, Poker table</li>
    <li>Great venues to host your next party, open 24/7 free to use and bookable by residents for free!</li>
    <li>Monthly resident events and parties hosted by the on-site staff</li>
    <li>Underground secured guest and resident parking available</li>
  </ul>

  <h2 class="section-title section-title--amenities">Apartment<br><em>Amenities</em></h2>
  <span class="rule rule--amenities"></span>
  <ul class="list list--amenities">
    <li>Gourmet Kitchen with 4&nbsp;piece Stainless Steel</li>
    <li>Appliances (Stove, Fridge, Microwave and Dishwasher)</li>
    <li>In suite dryer and washer</li>
    <li>Large Closets</li>
    <li>Patio/Balcony</li>
    <li>City and mountain views</li>
    <li>Ceramic Tile and Lami&shy;nate Hardwood Flooring</li>
    <li>Quartz Counter-tops</li>
    <li>Roller Blinds for all Windows</li>
  </ul>

  <div class="contact contact--phone">
    <svg width="22" height="18" viewBox="0 0 22 18" aria-hidden="true"><path d="M2 6 C2 2 20 2 20 6 L17 8 L15 5 H7 L5 8 Z" fill="var(--orange)"/><rect x="4" y="9" width="14" height="8" rx="2" fill="var(--orange)"/></svg>
    <span>+1 800-555-0142</span>
  </div>
  <div class="contact contact--web">
    <svg width="22" height="20" viewBox="0 0 20 20" aria-hidden="true"><circle cx="10" cy="10" r="9" fill="var(--orange)"/><path d="M1 10 H19 M10 1 V19 M10 1 C5 6 5 14 10 19 M10 1 C15 6 15 14 10 19" stroke="var(--paper)" stroke-width="1.2" fill="none"/></svg>
    <span>www.stayatthefenwick.example</span>
  </div>
  <div class="contact contact--address">
    <svg width="14" height="20" viewBox="0 0 14 20" aria-hidden="true"><path d="M7 0 C3 0 0 3 0 7 C0 12 7 20 7 20 C7 20 14 12 14 7 C14 3 11 0 7 0 Z" fill="var(--orange)"/><circle cx="7" cy="7" r="3" fill="var(--paper)"/></svg>
    <span>48 1190th Avenue SW<br>Calgary, Alberta T0X 0X0</span>
  </div>
  <div class="contact contact--social">
    <svg width="14" height="18" viewBox="0 0 14 18" aria-hidden="true"><path d="M12 0 L2 10 H7 L4 18 L13 6 H8 Z" fill="var(--orange)"/></svg>
    <span>https://social.example/<br>stayatthefenwick/</span>
  </div>
</main>
</body>
</html>
```